Brimvale Crest Homes needs a business card

We need a business card for a new company in Canada, Ontario. Our company is all about luxury contraction homes for our clients. Our product and services are custom projects design. Under the business logo that will be created, we want a slogan that will be a memorable phrase for consumers to remember us to tell their friends and relatives.

Additional infomation
- Teodoro Vanlesky
- President / Ceo
-519.304.7718

Find point what luxury construction products and services can be done

We like to see colors:
- #663300
- and something other colors or color that would attract the client needs and wants

The final design should communicate leads from new or old clients that will grow our empire. Most of all, we try to work among the budget that clients want

NOTE
- we also need an icon for the business (Example: Instagram, Facebook, and Whatsapp icons)
- We want the company name to be remembered easily for clients and our distributors who would get our orders.
- we need an icon on the business cards: Facebook and Instagram.

Thanks,
Brimvale Crest Homes

```html
<!DOCTYPE html>
<html lang="en">
<head>
<meta charset="utf-8">
<title>Brimvale Crest Homes – Business Card</title>
<link href="https://fonts.googleapis.com/css2?family=Questrial&display=swap" rel="stylesheet">
<style>
  :root {
    --bg: #141414;
    --bg-glow: #262626;
    --card: #0b0b0b;
    --card-edge: #1c1c1c;
    --brown: #663300;
    --brown-soft: #7a4514;
    --text: #e6e6e6;
    --text-dim: #bdbdbd;
  }
  * { box-sizing: border-box; margin: 0; padding: 0; }
  html, body { width: 1200px; height: 900px; overflow: hidden; }
  body {
    background: radial-gradient(ellipse at 50% 40%, var(--bg-glow) 0%, var(--bg) 70%);
    font-family: "Questrial", "Century Gothic", sans-serif;
    color: var(--text);
    position: relative;
  }
  .card {
    position: absolute;
    width: 500px;
    height: 286px;
    border-radius: 22px;
    background: var(--card);
    border: 1px solid var(--card-edge);
    box-shadow: 0 24px 50px rgba(0,0,0,.6);
    overflow: hidden;
  }
  .card--back { left: 640px; top: 90px; }
  .card--front { left: 80px; top: 380px; }

  /* front */
  .holder { position: absolute; left: 34px; top: 30px; }
  .holder__name { font-size: 27px; letter-spacing: .3px; color: var(--text); }
  .holder__title { margin-top: 4px; font-size: 12px; color: var(--brown-soft); letter-spacing: .4px; }
  .divider {
    position: absolute; left: 34px; top: 96px; width: 240px; height: 1px;
    background: var(--brown);
  }
  .contact { position: absolute; left: 34px; top: 176px; list-style: none; font-size: 12.5px; color: var(--text); }
  .contact li { display: flex; align-items: center; gap: 8px; margin-bottom: 9px; }
  .contact svg { width: 11px; height: 11px; fill: var(--brown-soft); }
  .band {
    position: absolute; left: 0; right: 0; bottom: 0; height: 38px;
    background: var(--brown);
    display: flex; align-items: center; padding-left: 42px;
    font-size: 13px; letter-spacing: .6px; color: #1a0d00;
  }
  .band__sep { margin: 0 12px; }

  /* brand lockup */
  .brand { position: absolute; display: flex; align-items: center; gap: 10px; }
  .brand__mark { width: 12px; height: 12px; background: var(--brown); }
  .brand__name { font-size: 17px; letter-spacing: 1px; color: var(--text); text-transform: uppercase; white-space: nowrap; }
  .card--front .brand { right: 30px; top: 88px; }
  .card--back .brand { right: 30px; bottom: 34px; }

  /* back */
  .services { position: absolute; left: 34px; top: 30px; list-style: none; font-size: 13px; color: var(--text-dim); }
  .services li { display: flex; align-items: center; gap: 8px; margin-bottom: 7px; }
  .services svg { width: 11px; height: 11px; }

  .showcase { position: absolute; right: 60px; bottom: 50px; }
  .showcase .brand { position: static; }
  .showcase .brand__name { font-size: 26px; }
  .showcase .brand__mark { width: 16px; height: 16px; }
</style>
</head>
<body>

<section class="card card--back" aria-label="Business card back">
  <ul class="services">
    <li><svg viewBox="0 0 12 12"><path d="M1 6.5l3 3L11 2" fill="none" stroke="#663300" stroke-width="2"/></svg>Custom Project Designs</li>
    <li><svg viewBox="0 0 12 12"><path d="M1 6.5l3 3L11 2" fill="none" stroke="#663300" stroke-width="2"/></svg>Home Renovations</li>
    <li><svg viewBox="0 0 12 12"><path d="M1 6.5l3 3L11 2" fill="none" stroke="#663300" stroke-width="2"/></svg>Kitchen remodeling</li>
    <li><svg viewBox="0 0 12 12"><path d="M1 6.5l3 3L11 2" fill="none" stroke="#663300" stroke-width="2"/></svg>Extiror Design / Interior Design</li>
    <li><svg viewBox="0 0 12 12"><path d="M1 6.5l3 3L11 2" fill="none" stroke="#663300" stroke-width="2"/></svg>Additions</li>
    <li><svg viewBox="0 0 12 12"><path d="M1 6.5l3 3L11 2" fill="none" stroke="#663300" stroke-width="2"/></svg>Garages</li>
    <li><svg viewBox="0 0 12 12"><path d="M1 6.5l3 3L11 2" fill="none" stroke="#663300" stroke-width="2"/></svg>Basements &amp; Bathrooms</li>
  </ul>
  <div class="brand">
    <span class="brand__mark"></span>
    <span class="brand__name">Brimvale Crest Homes</span>
  </div>
</section>

<section class="card card--front" aria-label="Business card front">
  <div class="holder">
    <h1 class="holder__name">Teodoro Vanlesky</h1>
    <p class="holder__title">President &nbsp;/&nbsp; Ceo</p>
  </div>
  <div class="divider"></div>
  <div class="brand">
    <span class="brand__mark"></span>
    <span class="brand__name">Brimvale Crest Homes</span>
  </div>
  <ul class="contact">
    <li><svg viewBox="0 0 12 12"><path d="M3 0.5l2 2.5-1.2 1.5c.7 1.6 2 2.9 3.7 3.7L9 7l2.5 2-1.3 2.3C5 11 1 7 .7 1.8z"/></svg>519.304.7718</li>
    <li><svg viewBox="0 0 12 12"><path d="M0 2h12v8H0z M0 2l6 4.5L12 2" fill="#7a4514" stroke="#0b0b0b" stroke-width=".8"/></svg>info@brimvalecrest.ca</li>
  </ul>
  <div class="band">HOME RENOVATIONS<span class="band__sep">|</span>CUSTOM PROJECT DESIGN</div>
</section>

<div class="showcase">
  <div class="brand">
    <span class="brand__mark"></span>
    <span class="brand__name">Brimvale Crest Homes</span>
  </div>
</div>

</body>
</html>
```